Local Roofing Company Billboard Design

We need a billboard design for an 8' x 32' billboard. This billboard would need to be easily readable and stand out well.
I have uploaded a design that we like - simple, readable, and gets the point across. We do NOT want the $1000 off offer included.
We are looking for a black background with white copy so it will stand out. We want the following on the billboard:
Kessler Roofing logo
kessler-roofing.example (optional)
555.271.6384 (mandatory)
Photo is optional, depends on how it all lays out
Production file must comply with layout requirements (uploaded).
Target Market(s)
Homeowners
Font styles to use
Other font styles liked:
- match font from logo
Colors
Designer to choose colors to be used in the design.
Requirements
Must have
- Black background, white copy, logo must be large and legible. Colors used must match our logo colors.

```html
<!DOCTYPE html>
<html lang="en">
<head>
<meta charset="utf-8">
<title>Kessler Roofing Billboard</title>
<link rel="stylesheet" href="https://fonts.googleapis.com/css2?family=Arvo:wght@700&family=Rubik:wght@600&display=swap">
<style>
  :root {
    --ink: #222222;
    --paper: #ffffff;
    --roof-orange: #e2622d;
    --shingle-light: #a9abad;
    --shingle-dark: #5d6063;
    --seal-navy: #1f2f6e;
  }
  html, body {
    margin: 0;
    width: 1200px;
    height: 866px;
    overflow: hidden;
    background: var(--paper);
  }
  .billboard {
    position: absolute;
    left: 0;
    top: 269px;
    width: 1200px;
    height: 327px;
    display: block;
  }
  .brand-name, .web-address {
    font-family: "Arvo", Georgia, serif;
    font-weight: 700;
    fill: var(--paper);
  }
  .phone-number {
    font-family: "Rubik", Arial, sans-serif;
    font-weight: 600;
    fill: var(--paper);
  }
</style>
</head>
<body>
<svg class="billboard" viewBox="0 0 1188 324" xmlns="http://www.w3.org/2000/svg" aria-label="Kessler Roofing billboard">
  <defs>
    <linearGradient id="shingle-tone" x1="0" y1="0" x2="1" y2="1">
      <stop offset="0" stop-color="var(--shingle-light)"/>
      <stop offset="1" stop-color="var(--shingle-dark)"/>
    </linearGradient>
  </defs>

  <rect class="board-base" x="0" y="0" width="1188" height="324" fill="var(--ink)"/>

  <polygon class="corner-photo" points="0,0 38,0 0,145" fill="url(#shingle-tone)" role="img" aria-label="Close-up photo of grey roof shingles"/>
  <line class="corner-stripe" x1="40" y1="0" x2="0" y2="152" stroke="var(--roof-orange)" stroke-width="5"/>

  <polygon class="shingle-photo" points="794,0 1188,0 1188,240 736,240" fill="url(#shingle-tone)" stroke="var(--paper)" stroke-width="4" role="img" aria-label="Close-up photo of grey asphalt roof shingles"/>

  <circle class="certification-seal" cx="962" cy="136" r="68" fill="var(--seal-navy)"/>

  <text class="brand-name" x="362" y="174" text-anchor="middle" font-size="47">Kessler Roofing</text>

  <polygon class="phone-band" points="0,212 737,212 712,302 0,302" fill="var(--roof-orange)" stroke="var(--paper)" stroke-width="3"/>
  <text class="phone-number" x="363" y="285" text-anchor="middle" font-size="72">555.271.6384</text>

  <text class="web-address" x="963" y="292" text-anchor="middle" font-size="29">kessler-roofing.example</text>
</svg>
</body>
</html>
```